Keep Harbor Homes. Avoid short sale, foreclosure, repossession, negative credit inquires and all other negative actions associated with your real estate.

Call 844-27-LUMEN or info@keepharborhomes.example

```html
<!DOCTYPE html>
<html lang="en">
<head>
<meta charset="utf-8">
<title>Keep Harbor Homes – Postcard</title>
<link rel="stylesheet" href="https://fonts.googleapis.com/css2?family=Montserrat:wght@800;900&family=Source+Sans+3:wght@600;700&display=swap">
<style>
  :root {
    --page: #ecebe8;
    --panel: #2b2c31;
    --panel-deep: #1f2024;
    --photo-light: #c9cbd8;
    --photo-mid: #8d90a6;
    --photo-dark: #4d5066;
    --gold: #fbbf1d;
    --gold-deep: #f29a12;
    --red: #e11d22;
    --red-deep: #b8141a;
    --white: #ffffff;
    --rule: #9a9a9a;
    --card-white: #fdfdfd;
  }
  * { margin: 0; padding: 0; box-sizing: border-box; }
  html, body { width: 932px; height: 1200px; overflow: hidden; }
  body {
    background: var(--page);
    font-family: "Source Sans 3", "Arial Narrow", sans-serif;
    color: var(--white);
    position: relative;
  }
  .card {
    position: absolute;
    left: 113px;
    width: 706px;
    height: 476px;
    overflow: hidden;
    box-shadow: 0 6px 14px rgba(0,0,0,.25);
  }
  .card--front { top: 80px; }
  .card--back { top: 624px; background: var(--card-white); }

  /* front */
  .front-photo {
    position: absolute; inset: 0;
    background: linear-gradient(180deg, var(--photo-light) 0%, var(--photo-mid) 45%, var(--photo-dark) 80%, #6f7288 100%);
  }
  .front-panel {
    position: absolute; left: 16px; top: 0; width: 281px; height: 476px;
    background: linear-gradient(180deg, rgba(31,32,36,.96), rgba(43,44,49,.9));
  }
  .ribbon {
    position: absolute; right: -42px; top: 22px;
    width: 220px; height: 34px;
    background: var(--panel-deep);
    transform: rotate(38deg);
    font-family: "Montserrat", sans-serif; font-weight: 800;
    font-size: 16px; letter-spacing: 1px;
    text-align: center; line-height: 34px;
  }
  .brand-name {
    font-family: "Montserrat", sans-serif; font-weight: 900;
    color: var(--gold); text-transform: uppercase;
    line-height: 1.02; white-space: nowrap;
  }
  .front-panel .brand-name { position: absolute; left: 0; width: 281px; top: 20px; text-align: center; font-size: 36px; }
  .divider {
    position: absolute; height: 2px;
    background: linear-gradient(90deg, transparent, rgba(255,255,255,.85), transparent);
  }
  .avoid-title {
    font-family: "Montserrat", sans-serif; font-weight: 800;
    color: var(--red); text-transform: uppercase;
    position: absolute; line-height: 1;
  }
  .avoid-list { list-style: none; position: absolute; text-transform: uppercase; font-weight: 600; }
  .avoid-list li { display: flex; align-items: center; white-space: nowrap; }
  .tick { flex: none; margin-right: 8px; }
  .note { position: absolute; font-weight: 600; line-height: 1.2; }
  .call-bar {
    position: absolute;
    background: linear-gradient(180deg, var(--red), var(--red-deep));
    display: flex; align-items: center;
    font-weight: 600; white-space: nowrap;
  }
  .call-bar .item { display: flex; align-items: center; }
  .call-bar svg { margin-right: 8px; }

  .front-panel .avoid-title { left: 16px; top: 180px; font-size: 22px; }
  .front-panel .avoid-list { left: 14px; top: 214px; font-size: 18px; }
  .front-panel .avoid-list li { height: 30px; }
  .front-panel .note { left: 14px; top: 346px; font-size: 17px; width: 270px; }
  .card--front .call-bar {
    left: 0; top: 414px; width: 706px; height: 36px;
    font-size: 21px; padding-left: 30px; gap: 18px;
  }
  .front-base {
    position: absolute; left: 16px; top: 450px; width: 281px; height: 26px;
    background: var(--panel);
  }

  /* back */
  .back-photo {
    position: absolute; left: 0; top: 0; width: 353px; height: 124px;
    background: linear-gradient(135deg, #e9ebf3 0%, #a9adc4 50%, #5f6380 100%);
  }
  .back-panel {
    position: absolute; left: 0; top: 124px; width: 353px; height: 352px;
    background: var(--panel);
  }
  .back-panel .brand-name { position: absolute; left: 18px; top: 20px; font-size: 23px; }
  .back-panel .avoid-title { left: 22px; top: 80px; font-size: 20px; }
  .back-panel .avoid-list { left: 20px; top: 108px; font-size: 17px; }
  .back-panel .avoid-list li { height: 26px; }
  .back-panel .note { left: 0; width: 353px; text-align: center; top: 220px; font-size: 15.5px; }
  .card--back .call-bar {
    left: 0; top: 266px; width: 353px; height: 40px;
    justify-content: center; font-size: 24px; gap: 18px;
    box-shadow: 0 4px 8px rgba(0,0,0,.35);
  }
  .back-email { position: absolute; left: 0; width: 353px; top: 318px; text-align: center; font-size: 15px; line-height: 20px; }
  .stamp-box {
    position: absolute; left: 592px; top: 24px; width: 92px; height: 62px;
    border: 2px solid var(--rule);
  }
  .address-line { position: absolute; left: 392px; width: 294px; height: 2px; background: var(--rule); }
</style>
</head>
<body>
  <svg width="0" height="0" style="position:absolute">
    <defs>
      <symbol id="tick" viewBox="0 0 16 16">
        <circle cx="8" cy="8" r="8" fill="#fbbf1d"/>
        <path d="M4.5 8.2l2.3 2.3 4.7-4.8" fill="none" stroke="#2b2c31" stroke-width="1.8" stroke-linecap="round" stroke-linejoin="round"/>
      </symbol>
      <symbol id="phone" viewBox="0 0 20 20">
        <rect width="20" height="20" rx="3" fill="#fbbf1d"/>
        <path d="M6.2 4.5l2 2.4-1.2 1.6c.8 1.7 2 2.9 3.6 3.7l1.6-1.2 2.4 2-1.1 2.2c-4.6-.5-8.2-4.1-8.6-8.6z" fill="#e11d22"/>
      </symbol>
      <symbol id="mail" viewBox="0 0 20 20">
        <rect width="20" height="20" rx="3" fill="#fbbf1d"/>
        <rect x="4" y="6" width="12" height="8.5" fill="#e11d22"/>
        <path d="M4 6l6 5 6-5" fill="none" stroke="#fbbf1d" stroke-width="1.3"/>
      </symbol>
    </defs>
  </svg>

  <section class="card card--front">
    <div class="front-photo" role="img" aria-label="Photo of a two-storey suburban house with porch and front lawn, in cool blue-grey tones"></div>
    <div class="ribbon">FORECLOSURE</div>
    <div class="front-panel">
      <h1 class="brand-name">Keep<br>Harbor<br>Homes</h1>
      <div class="divider" style="left:60px;top:156px;width:160px"></div>
      <h2 class="avoid-title">Avoid</h2>
      <ul class="avoid-list">
        <li><svg class="tick" width="16" height="16"><use href="#tick"/></svg>Short sale</li>
        <li><svg class="tick" width="16" height="16"><use href="#tick"/></svg>Foreclosure</li>
        <li><svg class="tick" width="16" height="16"><use href="#tick"/></svg>Repossession</li>
        <li><svg class="tick" width="16" height="16"><use href="#tick"/></svg>Negative credit inquires</li>
      </ul>
      <p class="note">and all other negative actions<br>associated with your real estate.</p>
    </div>
    <div class="call-bar">
      <span>CALL</span>
      <span class="item"><svg width="20" height="20"><use href="#phone"/></svg>844-27-LUMEN</span>
      <span>or</span>
      <span class="item"><svg width="20" height="20"><use href="#mail"/></svg>info@keepharborhomes.example</span>
    </div>
    <div class="front-base"></div>
  </section>

  <section class="card card--back">
    <div class="back-photo" role="img" aria-label="Photo of a small model house on a desk beside hands signing documents, in cool grey-blue tones"></div>
    <div class="back-panel">
      <h1 class="brand-name">Keep Harbor Homes</h1>
      <div class="divider" style="left:40px;top:62px;width:270px"></div>
      <h2 class="avoid-title">Avoid</h2>
      <ul class="avoid-list">
        <li><svg class="tick" width="14" height="14"><use href="#tick"/></svg>Short sale</li>
        <li><svg class="tick" width="14" height="14"><use href="#tick"/></svg>Foreclosure</li>
        <li><svg class="tick" width="14" height="14"><use href="#tick"/></svg>Repossession</li>
        <li><svg class="tick" width="14" height="14"><use href="#tick"/></svg>Negative credit inquires</li>
      </ul>
      <p class="note">and all other negative actions associated<br>with your real estate.</p>
      <div class="call-bar">
        <span>CALL</span>
        <span class="item"><svg width="20" height="20"><use href="#phone"/></svg>844-27-LUMEN</span>
      </div>
      <p class="back-email">info@keepharborhomes.example</p>
    </div>
    <div class="stamp-box"></div>
    <div class="address-line" style="top:188px"></div>
    <div class="address-line" style="top:230px"></div>
    <div class="address-line" style="top:272px"></div>
  </section>
</body>
</html>
```